Business card design needed

We need a buisness card design to suit our buisness "Bright Parcels", a company on the south coast of Australia, a wholesale greeting card and gift wrap buisness. We are open to different colour options possibly some pastels. A card that got my attention was'the ''trackbeacon.com.au'' buisness card. I liked the colour scheme, layout, and the use of a cartoon image, but am also open to all ideas.

Industry/Entity Type

Business

Contact Information for Business Card

Bright Parcels Unit 31 / 17 Morwell ave Kelston Point 2598 ph 0247835108 fax 0247835109 Colin Maskey email bright.parcels@mailverra.com

```html
<!DOCTYPE html>
<html lang="en">
<head>
<meta charset="utf-8">
<title>Bright Parcels – Business Card</title>
<link href="https://fonts.googleapis.com/css2?family=Open+Sans:wght@400;600;700&display=swap" rel="stylesheet">
<style>
  :root {
    --teal: #0c5d6c;
    --teal-deep: #084a57;
    --peach: #f2bc93;
    --green: #5bb247;
    --paper: #f7f6f3;
    --paper-warm: #efe6dd;
    --ink: #2f3a3d;
    --backdrop: #e4e6e7;
  }
  * { box-sizing: border-box; margin: 0; padding: 0; }
  html, body { width: 1200px; height: 900px; overflow: hidden; }
  body {
    background: var(--backdrop);
    font-family: "Open Sans", Arial, sans-serif;
    display: flex;
    align-items: center;
    justify-content: center;
    gap: 40px;
  }
  .card {
    position: relative;
    width: 520px;
    height: 297px;
    border-radius: 3px;
    box-shadow: 0 6px 18px rgba(0,0,0,0.18);
    overflow: hidden;
  }

  /* Back of card */
  .card-back {
    background: linear-gradient(160deg, var(--teal) 0%, var(--teal-deep) 100%);
    display: flex;
    align-items: center;
    justify-content: center;
  }
  .card-back .brand-name {
    color: var(--peach);
    font-weight: 600;
    font-size: 34px;
  }

  /* Front of card */
  .card-front {
    background: linear-gradient(135deg, var(--paper) 0%, #ffffff 45%, var(--paper-warm) 100%);
  }
  .card-front .header-swoosh {
    position: absolute;
    inset: 0;
    width: 100%;
    height: 100%;
  }
  .card-front .brand-name {
    position: absolute;
    top: 26px;
    right: 36px;
    color: #ffffff;
    font-weight: 600;
    font-size: 22px;
    white-space: nowrap;
  }
  .contact-block {
    position: absolute;
    left: 30px;
    top: 136px;
    width: 340px;
  }
  .contact-block .rule {
    height: 1px;
    background: var(--teal);
    opacity: 0.5;
    width: 300px;
    margin-bottom: 6px;
  }
  .contact-block .person-name {
    color: var(--teal);
    font-weight: 700;
    font-size: 24px;
    line-height: 1.15;
    white-space: nowrap;
    padding-bottom: 5px;
    border-bottom: 1px solid rgba(12,93,108,0.35);
    width: 170px;
    margin-bottom: 8px;
  }
  .contact-list { list-style: none; }
  .contact-list li {
    display: flex;
    align-items: center;
    gap: 8px;
    font-size: 11.5px;
    color: var(--ink);
    line-height: 17px;
    white-space: nowrap;
  }
  .contact-list svg { width: 11px; height: 11px; flex: none; fill: var(--green); }
</style>
</head>
<body>

  <section class="card card-back" aria-label="Business card back">
    <span class="brand-name">BrightParcels</span>
  </section>

  <section class="card card-front" aria-label="Business card front">
    <svg class="header-swoosh" viewBox="0 0 520 297" preserveAspectRatio="none" aria-hidden="true">
      <path d="M166,0 C222,80 320,92 520,96 L520,88 C320,82 230,70 176,0 Z" fill="var(--green)"/>
      <path d="M176,0 C230,70 320,82 520,88 L520,0 Z" fill="var(--teal)"/>
    </svg>
    <span class="brand-name">BrightParcels</span>

    <div class="contact-block">
      <div class="rule"></div>
      <div class="person-name">Colin Maskey</div>
      <ul class="contact-list">
        <li>
          <svg viewBox="0 0 24 24" aria-hidden="true"><path d="M6.6 10.8a15 15 0 0 0 6.6 6.6l2.2-2.2a1 1 0 0 1 1-.25 11.4 11.4 0 0 0 3.6.57 1 1 0 0 1 1 1V20a1 1 0 0 1-1 1A17 17 0 0 1 3 4a1 1 0 0 1 1-1h3.5a1 1 0 0 1 1 1c0 1.25.2 2.45.57 3.57a1 1 0 0 1-.25 1z"/></svg>
          0247-835-108
        </li>
        <li>
          <svg viewBox="0 0 24 24" aria-hidden="true"><path d="M6 2h10l2 2v5H6z M3 10h18v8h-3v4H6v-4H3z M8 15v5h8v-5z"/></svg>
          0247-835-109
        </li>
        <li>
          <svg viewBox="0 0 24 24" aria-hidden="true"><path d="M2 5h20v14H2z M3.5 6.5 12 13l8.5-6.5z" fill-rule="evenodd"/></svg>
          bright.parcels@mailverra.com
        </li>
        <li>
          <svg viewBox="0 0 24 24" aria-hidden="true"><path d="M12 2a7 7 0 0 0-7 7c0 5 7 13 7 13s7-8 7-13a7 7 0 0 0-7-7zm0 9.5A2.5 2.5 0 1 1 12 6.5a2.5 2.5 0 0 1 0 5z"/></svg>
          Unit 31 / 17 Morwell ave Kelston Point 2598
        </li>
      </ul>
    </div>
  </section>

</body>
</html>
```